Korvane Pty Ltd professional business card

A professional business card template using the colours from the supplied logo.
Clean crisp lines while, Modern while not being over the top.

Target Market(s)

Construction, commerical and industrial

Industry/Entity Type

Communications

Contact Information for Business Card

For a Communications, IT, Optical fibre installation company

Colors
37b8a4

```html
<!DOCTYPE html>
<html lang="en">
<head>
<meta charset="utf-8">
<title>Korvane Pty Ltd – Business Card</title>
<link rel="stylesheet" href="https://fonts.googleapis.com/css2?family=Montserrat:wght@500;600;700&family=Roboto:wght@400&display=swap">
<style>
  :root {
    --backdrop: #2b2b2c;
    --card: #1f2022;
    --card-edge: #18191a;
    --teal: #37b8a4;
    --grey-text: #9a9b9d;
    --logo-grey: #8a8b8d;
    --rule: #5a5b5d;
    --pattern-top: #26272a;
    --pattern-bottom: #1c1d1f;
  }
  * { margin: 0; padding: 0; box-sizing: border-box; }
  html, body { width: 1200px; height: 1108px; overflow: hidden; }
  body {
    background: var(--backdrop);
    display: flex;
    justify-content: center;
    align-items: center;
    gap: 80px;
    font-family: "Roboto", Arial, sans-serif;
  }
  .card {
    width: 400px;
    height: 620px;
    border-radius: 26px;
    background: var(--card);
    box-shadow: 0 14px 30px rgba(0,0,0,.45);
    position: relative;
    overflow: hidden;
  }
  .card-front {
    display: flex;
    flex-direction: column;
    align-items: center;
    padding-top: 150px;
    text-align: center;
  }
  .brand {
    display: flex;
    align-items: center;
    gap: 12px;
    font-family: "Montserrat", Arial, sans-serif;
    font-weight: 600;
    font-size: 46px;
    letter-spacing: 1px;
    color: var(--logo-grey);
  }
  .brand-mark {
    width: 22px; height: 22px;
    background: var(--teal);
  }
  .person-name {
    margin-top: 56px;
    font-family: "Montserrat", Arial, sans-serif;
    font-weight: 700;
    font-size: 21px;
    color: var(--teal);
    letter-spacing: .5px;
  }
  .person-role {
    font-size: 16px;
    color: var(--grey-text);
    margin-top: 2px;
  }
  .icon-row {
    margin-top: 14px;
    display: flex;
    align-items: center;
    gap: 6px;
  }
  .icon-row .rule {
    width: 46px;
    height: 1px;
    background: var(--rule);
    margin: 0 6px;
  }
  .icon {
    width: 24px; height: 24px;
    border: 1.5px solid var(--teal);
    display: flex; align-items: center; justify-content: center;
  }
  .icon svg { width: 15px; height: 15px; stroke: var(--teal); fill: none; stroke-width: 1.6; }
  .contact-list {
    list-style: none;
    margin-top: 12px;
    font-size: 16px;
    line-height: 22px;
    color: var(--grey-text);
  }
  .contact-list .accent { color: var(--teal); }
  .divider {
    width: 200px;
    height: 1px;
    background: var(--rule);
    margin: 12px 0 12px;
  }
  .company-name {
    font-family: "Montserrat", Arial, sans-serif;
    font-weight: 700;
    font-size: 17px;
    color: var(--teal);
  }
  .address {
    font-style: normal;
    font-size: 16px;
    line-height: 21px;
    color: var(--grey-text);
  }
  .card-back .pattern-area {
    position: absolute;
    inset: 0 0 150px 0;
    background: linear-gradient(180deg, var(--pattern-top), var(--pattern-bottom));
  }
  .card-back .brand {
    position: absolute;
    left: 0; right: 0; bottom: 70px;
    justify-content: center;
  }
</style>
</head>
<body>
  <section class="card card-front">
    <div class="brand"><span class="brand-mark"></span>KORVANE</div>
    <h1 class="person-name">DANIEL HARPER</h1>
    <p class="person-role">Managing Director</p>
    <div class="icon-row">
      <span class="rule"></span>
      <span class="icon" aria-label="phone"><svg viewBox="0 0 16 16"><path d="M4 2h3l1 3-2 1a8 8 0 0 0 4 4l1-2 3 1v3a1 1 0 0 1-1 1A12 12 0 0 1 3 3a1 1 0 0 1 1-1z"/></svg></span>
      <span class="icon" aria-label="fax"><svg viewBox="0 0 16 16"><rect x="2" y="6" width="12" height="6"/><path d="M5 6V2h6v4M5 12v2h6v-2"/></svg></span>
      <span class="icon" aria-label="email"><svg viewBox="0 0 16 16"><rect x="2" y="4" width="12" height="8"/><path d="M2 4l6 5 6-5"/></svg></span>
      <span class="icon" aria-label="website"><svg viewBox="0 0 16 16"><circle cx="8" cy="8" r="6"/><path d="M2 8h12M8 2c-3 3-3 9 0 12M8 2c3 3 3 9 0 12"/></svg></span>
      <span class="rule"></span>
    </div>
    <ul class="contact-list">
      <li>044-987 650 312</li>
      <li>044-987 650 312</li>
      <li>info@korvane.com</li>
      <li>www.<span class="accent">korvane</span>.com</li>
    </ul>
    <div class="divider"></div>
    <p class="company-name">Korvane Pty Ltd</p>
    <address class="address">12345, Address Goes Here<br>Country Name, 123456</address>
  </section>

  <section class="card card-back">
    <div class="pattern-area" role="img" aria-label="Faint repeating brand pattern"></div>
    <div class="brand"><span class="brand-mark"></span>KORVANE</div>
  </section>
</body>
</html>
```